i need a business card to promote my Handyman & Gardening business. It would be nice to see a design incorporating both of these things. We are happy to help in any way we can with no job ever being to small.

Dave's Handyman & Gardening Service
Dave Holt
PO Box 417 Ferndale SA 5999
dave.holt@fernmail.com
ph 0412 738 265

```html
<!DOCTYPE html>
<html lang="en">
<head>
<meta charset="utf-8">
<title>Dave's Handyman &amp; Gardening Service – Business Card</title>
<link href="https://fonts.googleapis.com/css2?family=Oswald:wght@700&family=Questrial&display=swap" rel="stylesheet">
<style>
  :root {
    --page-bg: #ffffff;
    --silver-light: #f4f4f4;
    --silver-mid: #d9d9d9;
    --silver-dark: #a9a9a9;
    --orange: #e2541e;
    --orange-deep: #c9441a;
    --ink: #111111;
    --panel-dark: #1a1a1a;
    --panel-black: #050505;
    --text-light: #e6e6e6;
    --text-muted: #a8a8a8;
  }
  * { box-sizing: border-box; margin: 0; padding: 0; }
  html, body {
    width: 1200px;
    height: 900px;
    overflow: hidden;
    background: var(--page-bg);
  }
  .business-card {
    position: absolute;
    left: 100px;
    top: 150px;
    width: 1000px;
    height: 600px;
    border-radius: 40px;
    overflow: hidden;
    background: var(--panel-black);
    box-shadow: 0 10px 30px rgba(0,0,0,0.18);
  }
  .card-header {
    position: absolute;
    left: 0; top: 0;
    width: 100%;
    height: 280px;
    background: linear-gradient(180deg, var(--silver-dark) 0%, var(--silver-light) 45%, var(--silver-mid) 100%);
  }
  .tools-art {
    position: absolute;
    border-radius: 12px;
  }
  .tools-art--handyman {
    left: 14px; top: 36px;
    width: 220px; height: 230px;
    background: radial-gradient(ellipse at 45% 50%, #3a3a3a 0%, #6a6a6a 45%, rgba(200,200,200,0) 75%);
  }
  .tools-art--garden {
    right: 18px; top: 40px;
    width: 200px; height: 225px;
    background: radial-gradient(ellipse at 50% 50%, #5b4a44 0%, #a06040 35%, rgba(200,200,200,0) 72%);
  }
  .brand {
    position: absolute;
    left: 230px;
    top: 40px;
    width: 560px;
    text-align: center;
  }
  .brand-name {
    font-family: "Oswald", sans-serif;
    font-weight: 700;
    font-size: 118px;
    line-height: 1;
    color: var(--orange);
  }
  .brand-service {
    margin-top: 16px;
    font-family: "Oswald", sans-serif;
    font-weight: 700;
    font-size: 36px;
    line-height: 1;
    color: var(--ink);
    text-transform: uppercase;
    white-space: nowrap;
  }
  .tagline-band {
    position: absolute;
    left: 0; top: 280px;
    width: 100%;
    height: 36px;
    background: linear-gradient(180deg, var(--orange) 0%, var(--orange-deep) 100%);
    display: flex;
    align-items: center;
    justify-content: space-between;
    padding: 0 40px;
    font-family: "Oswald", sans-serif;
    font-weight: 700;
    font-size: 24px;
    color: var(--ink);
    text-transform: uppercase;
  }
  .contact-panel {
    position: absolute;
    left: 0; top: 316px;
    width: 100%;
    height: 284px;
    background: linear-gradient(180deg, var(--panel-black) 0%, var(--panel-dark) 55%, var(--panel-black) 100%);
    text-align: center;
    font-family: "Questrial", sans-serif;
  }
  .contact-name {
    margin-top: 30px;
    font-size: 48px;
    color: var(--orange);
  }
  .contact-phone {
    margin-top: 26px;
    font-size: 40px;
    color: var(--text-light);
    letter-spacing: 1px;
  }
  .contact-email {
    margin-top: 8px;
    font-size: 34px;
    color: var(--text-light);
  }
  .contact-address {
    margin-top: 8px;
    font-size: 34px;
    color: var(--text-muted);
  }
</style>
</head>
<body>
  <article class="business-card">
    <header class="card-header">
      <div class="tools-art tools-art--handyman" role="img" aria-label="Illustration of handyman tools: hammer, tape measure, pliers and wrench"></div>
      <div class="brand">
        <h1 class="brand-name">Dave's</h1>
        <p class="brand-service">Handyman &amp; Gardening Service</p>
      </div>
      <div class="tools-art tools-art--garden" role="img" aria-label="Illustration of gardening tools: trowel, hand rake, pruning shears and saw"></div>
    </header>
    <div class="tagline-band" aria-label="No job is too small">
      <span>N</span><span>O</span><span></span><span>J</span><span>O</span><span>B</span><span></span><span>I</span><span>S</span><span></span><span>T</span><span>O</span><span>O</span><span></span><span>S</span><span>M</span><span>A</span><span>L</span><span>L</span>
    </div>
    <section class="contact-panel">
      <p class="contact-name">Dave Holt</p>
      <p class="contact-phone">0412 738 265</p>
      <p class="contact-email">dave.holt@fernmail.com</p>
      <p class="contact-address">PO Box 417 Ferndale SA 5999</p>
    </section>
  </article>
</body>
</html>
```